Permanent Makeup (cosmetics salon) Brochure

We need a 2-4 sites brochure for our Permanent Makeup (cosmetics salon). Our company is based in Austria / Vienna. -> Our homepage is www.mk-lorenzhuber.at
This brochure should show which treatments we provide ot our customers.

I've uploaded our old brochure, the content (text) would be nearly the same (look form "Must Haves", pics have to be new (look uploaded pics)
The old brochure is to dark. -> look for our homepage maybe you can make it like this

Target Market(s)

woman, age 25-70 years who wants to have permanent makeup on eyebrows, lips or eyeliner

Industry/Entity Type

Beauty Salon

Requirements
Must have
• pics which are uploaded.

*This text (somithing about our business)
"Für Frau Lorenzhuber ist Permanent Makeup ein Kunsthandwerk. Das Team von MK-Lorenzhuber ist spezialisiert auf natürliches Permanent Makeup damit der individuelle Typ jeder Kundin am schönsten zum Ausdruck kommt."

*We do this treatments: (english)
+ Augenbrauen Microblading (eyebrows)
+ Augenbrauen Permanent Makeup (eyebrows2)
+ Lidstrich Permanent Makeup (eyeliner)
+ Lip Blushing (lips)
+ Lippen Permanent Makeup (lips2)

* Our addresses (2 locations)
Wien
Kerngasse 7b/12, 1010 Wien
Tel: 01/5827316

Villach
Birkenhofweg 24, 9524 St. Ulrich
Tel: 0676/3158940

Mail: info@mk-lorenzhuber.at
www.mk-lorenzhuber.at

```html
<!DOCTYPE html>
<html lang="de">
<head>
<meta charset="utf-8">
<title>Milena Lorenzhuber Kosmetikstudio – Broschüre</title>
<link rel="stylesheet" href="https://fonts.googleapis.com/css2?family=Josefin+Sans:wght@300;400&family=Great+Vibes&display=swap">
<style>
  :root {
    --backdrop: #bcbdbf;
    --paper: #ffffff;
    --ink: #111111;
    --ink-soft: #2a2a2a;
    --gold: #d2ad4a;
    --gold-light: #e6c96e;
    --gold-dark: #b88f2c;
    --black: #000000;
  }
  * { box-sizing: border-box; margin: 0; padding: 0; }
  html, body { width: 783px; height: 1200px; overflow: hidden; }
  body {
    position: relative;
    background: var(--backdrop);
    font-family: "Josefin Sans", sans-serif;
    font-weight: 300;
    color: var(--ink);
  }
  .page {
    position: absolute;
    background: var(--paper);
    box-shadow: 0 2px 5px rgba(0,0,0,0.18);
    overflow: hidden;
  }
  .cover { left: 66px; top: 112px; width: 320px; height: 320px; }
  .spread { left: 66px; top: 451px; width: 639px; height: 320px; }
  .back { left: 386px; top: 795px; width: 320px; height: 320px; }

  .photo { position: absolute; }
  .abs { position: absolute; }

  /* brand line */
  .brand { position: absolute; text-align: center; transform: translateX(-50%); }
  .brand-name {
    display: flex; align-items: center; justify-content: center; gap: 5px;
    font-size: 11px; font-weight: 400; color: var(--ink); white-space: nowrap; letter-spacing: 0.3px;
  }
  .brand-dot {
    width: 20px; height: 20px; border-radius: 50%;
    border: 2px solid var(--gold);
  }
  .brand-sub { font-size: 3.6px; font-weight: 400; letter-spacing: 1.6px; margin-top: 3px; }

  .gold-band {
    position: absolute;
    background: linear-gradient(90deg, var(--gold-dark), var(--gold-light) 50%, var(--gold));
    color: var(--ink-soft);
    font-size: 5.6px; font-weight: 400;
    display: flex; align-items: center; justify-content: center; gap: 4px;
    white-space: nowrap;
  }

  /* cover */
  .cover-headline { position: absolute; left: 0; width: 100%; text-align: center; font-weight: 300; line-height: 1; }
  .headline-main { top: 210px; font-size: 39px; letter-spacing: -0.5px; }
  .headline-mid { top: 253px; font-size: 11.5px; }
  .headline-end { top: 266px; font-size: 29px; }

  /* spread */
  .claim-box {
    left: 20px; top: 125px; width: 132px; height: 85px;
    background: var(--black); color: #fff; text-align: center;
  }
  .claim-line { font-size: 8.5px; margin-top: 21px; }
  .claim-script { font-family: "Great Vibes", cursive; color: var(--gold); font-size: 11px; line-height: 1; margin-top: 2px; }
  .claim-big { font-size: 16px; font-weight: 400; letter-spacing: 0.2px; margin-top: 1px; }

  .section-title { font-weight: 300; line-height: 1; }
  .about-title { left: 175px; top: 114px; font-size: 29px; }
  .about-text { left: 175px; top: 148px; width: 114px; font-size: 6.6px; line-height: 9.3px; color: var(--ink-soft); }

  .treat-kicker { left: 448px; top: 40px; font-size: 11px; }
  .treat-title { left: 447px; top: 55px; font-size: 33px; letter-spacing: -0.3px; }
  .treat-list { left: 352px; top: 118px; list-style: none; }
  .treat-list li {
    display: flex; align-items: center; gap: 5px;
    font-size: 6.8px; height: 14.5px; color: var(--ink-soft);
  }
  .treat-list li::before {
    content: ""; width: 5px; height: 5px; border-radius: 50%;
    border: 0.8px solid var(--gold); background: rgba(230,201,110,0.35);
  }

  /* back */
  .back-intro { left: 0; top: 36px; width: 100%; text-align: center; font-size: 6.8px; line-height: 9.5px; color: var(--ink-soft); }
  .location { font-size: 5.3px; line-height: 9px; color: var(--ink-soft); }
  .location-tag {
    display: inline-block; padding: 0 3px; height: 9px; line-height: 10px;
    background: linear-gradient(90deg, var(--gold-dark), var(--gold-light));
    color: #fff; font-size: 5.6px; margin-bottom: 2px;
  }
</style>
</head>
<body>

  <!-- Cover -->
  <section class="page cover">
    <div class="brand" style="left:160px; top:28px;">
      <div class="brand-name">Milena <span class="brand-dot"></span> Lorenzhuber</div>
      <div class="brand-sub">KOSMETIKSTUDIO</div>
    </div>
    <div class="photo" role="img" aria-label="Nahaufnahme eines Frauenauges mit blondem Haar"
         style="left:0; top:72px; width:320px; height:122px; background:linear-gradient(90deg,#eee0cf,#d9a78a 40%,#c98469 70%,#e8d2b8);"></div>
    <div class="cover-headline headline-main">Schönheit</div>
    <div class="cover-headline headline-mid">kommt nicht nur von</div>
    <div class="cover-headline headline-end">innen</div>
    <div class="gold-band" style="left:111px; top:299px; width:98px; height:9px;">www.mk-lorenzhuber.at</div>
  </section>

  <!-- Inner spread -->
  <section class="page spread">
    <div class="photo" role="img" aria-label="Augenpartie mit gepflegten Augenbrauen und braunen Augen"
         style="left:0; top:0; width:243px; height:97px; background:linear-gradient(90deg,#d7b3a0,#c99a84 50%,#dcc0b3);"></div>
    <div class="photo" role="img" aria-label="Auge und Augenbraue einer Frau mit dunklem Haar"
         style="left:253px; top:0; width:150px; height:97px; background:linear-gradient(90deg,#b7856b,#c6977c 60%,#4a3428);"></div>

    <div class="abs claim-box">
      <div class="claim-line">Macht jeden Augenblick zu</div>
      <div class="claim-script">einer</div>
      <div class="claim-big">AUGENWEIDE</div>
    </div>

    <h2 class="abs section-title about-title">About</h2>
    <p class="abs about-text">Für Frau Lorenzhuber ist Permanent Makeup ein Kunsthandwerk. Das Team von MK-Lorenzhuber ist spezialisiert auf natürliches Permanent Makeup damit der individuelle Typ jeder Kundin am schönsten zum Ausdruck kommt.</p>

    <div class="brand" style="left:100px; top:236px;">
      <div class="brand-name">Milena <span class="brand-dot"></span> Lorenzhuber</div>
      <div class="brand-sub">KOSMETIKSTUDIO</div>
    </div>
    <div class="gold-band" style="left:33px; top:284px; width:136px; height:9px;">
      <span>info@mk-lorenzhuber.at</span><span>|</span><span>www.mk-lorenzhuber.at</span>
    </div>

    <div class="abs treat-kicker">We do this</div>
    <h2 class="abs section-title treat-title">Treatments</h2>
    <ul class="abs treat-list">
      <li>Augenbrauen Microblading (eyebrows)</li>
      <li>Augenbrauen Permanent Makeup (eyebrows2)</li>
      <li>Lidstrich Permanent Makeup (eyeliner)</li>
      <li>Lip Blushing (lips)</li>
      <li>Lippen Permanent Makeup (lips2)</li>
    </ul>

    <div class="photo" role="img" aria-label="Nahaufnahme von Lippen mit rosafarbenem Permanent Makeup"
         style="left:320px; top:201px; width:165px; height:111px; background:linear-gradient(180deg,#d9a38c,#e08c84 55%,#dcb1a0);"></div>
    <div class="photo" role="img" aria-label="Nahaufnahme voller Lippen mit Lip Blushing"
         style="left:491px; top:201px; width:148px; height:111px; background:linear-gradient(180deg,#dba796,#d98a86 55%,#d9aa9c);"></div>
  </section>

  <!-- Back -->
  <section class="page back">
    <p class="abs back-intro">Ihr Kosmetikstudio und Beauty Salon in 1010 Wien Professionelles Microblading<br>und Permanent Make Up für gehobene Ansprüche</p>
    <div class="photo" role="img" aria-label="Auge mit langen Wimpern vor dunklem Hintergrund"
         style="left:0; top:73px; width:320px; height:122px; background:linear-gradient(90deg,#c59c86,#b98570 55%,#5a3a2c 80%,#140d0b);"></div>

    <div class="brand" style="left:88px; top:222px;">
      <div class="brand-name">Milena <span class="brand-dot"></span> Lorenzhuber</div>
      <div class="brand-sub">KOSMETIKSTUDIO</div>
    </div>

    <div class="abs location" style="left:35px; top:273px;">
      <span class="location-tag">Wien</span><br>
      Kerngasse 7b/12, 1010 Wien<br>
      Tel: 01/5827316
    </div>
    <div class="abs location" style="left:124px; top:273px;">
      <span class="location-tag">Villach</span><br>
      Birkenhofweg 24, 9524 St. Ulrich<br>
      Tel: 0676/3158940
    </div>
    <div class="abs location" style="left:233px; top:284px; line-height:8px;">
      info@mk-lorenzhuber.at<br>
      www.mk-lorenzhuber.at
    </div>
  </section>

</body>
</html>
```